I need beautiful business cards with Moonpetals and Sparrows on then and my tavolink business name is Moonpetals and sparrows.
I sell mini gardens, candles and melts and gift ware....on the other side I would like some thing like...REMEMBER to keep in touch with Moonpetals and sparrows buy a like,comment or just to say hello or tavo link will think you are no longer interested and delete you....you can change the wording to that to make smaller if you would like, and am not sure how to word it....my color theme for my business in purple and green. thank you.

tavo link:Moonpetals and sparrows
mini gardens
candles and melts
gift ware.
email:rosa514@kelvimail.com
phone:0873514062

```html
<!DOCTYPE html>
<html lang="en">
<head>
<meta charset="utf-8">
<title>Moonpetals and Sparrows – Business Card</title>
<link href="https://fonts.googleapis.com/css2?family=Cinzel:wght@400;500&family=Cutive&display=swap" rel="stylesheet">
<style>
  :root {
    --leaf-green: #a3c95b;
    --meadow-light: #d6e8b0;
    --meadow-mid: #c4de92;
    --lavender: #a47fba;
    --plum: #6b3f87;
    --plum-deep: #5a3476;
    --wing-light: #a67dc0;
    --wing-dark: #6d3f8c;
  }
  html, body {
    margin: 0;
    padding: 0;
    overflow: hidden;
    background: #ffffff;
  }
  .card {
    position: relative;
    width: 1200px;
    height: 668px;
    overflow: hidden;
    background: var(--leaf-green);
  }
  .meadow-dome {
    position: absolute;
    left: 0;
    top: 0;
    width: 1200px;
    height: 438px;
  }
  .tagline {
    font-family: "Cutive", serif;
    font-size: 41px;
    fill: var(--plum);
  }
  .illustration {
    position: absolute;
    border-radius: 50%;
  }
  .illustration--dragonfly {
    left: 344px;
    top: 232px;
    width: 256px;
    height: 164px;
    background: radial-gradient(ellipse at center, var(--wing-dark) 0%, var(--wing-light) 55%, rgba(166,125,192,0) 72%);
  }
  .illustration--butterfly {
    left: 626px;
    top: 158px;
    width: 254px;
    height: 232px;
    background: radial-gradient(ellipse at center, var(--wing-dark) 0%, var(--wing-light) 55%, rgba(166,125,192,0) 72%);
  }
  .accent-stripe {
    position: absolute;
    left: 0;
    top: 413px;
    width: 1200px;
    height: 25px;
    background: var(--lavender);
  }
  .name-band {
    position: absolute;
    left: 0;
    top: 438px;
    width: 1200px;
    height: 99px;
    background: var(--meadow-mid);
    display: flex;
    align-items: center;
    justify-content: center;
  }
  .business-name {
    margin: 0;
    font-family: "Cinzel", serif;
    font-weight: 400;
    font-size: 62px;
    letter-spacing: 1px;
    color: var(--plum);
    line-height: 1;
  }
  .contact-band {
    position: absolute;
    left: 0;
    top: 537px;
    width: 1200px;
    height: 131px;
    background: var(--lavender);
    display: flex;
    flex-direction: column;
    align-items: center;
    justify-content: center;
    gap: 6px;
  }
  .contact-line {
    margin: 0;
    font-family: "Cutive", serif;
    font-size: 38px;
    line-height: 1.15;
    color: var(--plum-deep);
  }
</style>
</head>
<body>
  <div class="card">
    <svg class="meadow-dome" viewBox="0 0 1200 438" width="1200" height="438">
      <defs>
        <radialGradient id="dome-glow" cx="50%" cy="75%" r="60%">
          <stop offset="0%" stop-color="#e4f0c8"/>
          <stop offset="100%" stop-color="#c6df93"/>
        </radialGradient>
        <path id="tagline-arc" d="M 100 340 Q 600 -90 1100 340"/>
      </defs>
      <path d="M 0 413 L 0 395 A 600 370 0 0 1 1200 395 L 1200 413 Z" fill="url(#dome-glow)"/>
      <text class="tagline">
        <textPath href="#tagline-arc" startOffset="50%" text-anchor="middle">mini gardens candles and melts gift ware</textPath>
      </text>
    </svg>

    <div class="illustration illustration--dragonfly" role="img" aria-label="Purple dragonfly illustration with soft shadow"></div>
    <div class="illustration illustration--butterfly" role="img" aria-label="Purple butterfly illustration with soft shadow"></div>

    <div class="accent-stripe"></div>

    <div class="name-band">
      <h1 class="business-name">Moonpetals and Sparrows</h1>
    </div>

    <div class="contact-band">
      <p class="contact-line">email: rosa514@kelvimail.com</p>
      <p class="contact-line">phone:0873514062</p>
    </div>
  </div>
</body>
</html>
```